Electrician Needs A Business Card

I already have a logo and would like a business card to be designed based around this logo the company is called Coralwood Electrical Pty Ltd

The business card will be printed on transparent plastic so I need it to stand out from the crowd. I do not want the card to have anything to do with Electrical on it eg light bulbs, power points etc

I need it to have the following details.

Dominic Farrow
Mobile : 0452 317 908
email : dominic@coralwoodelectrical.com.au

If it could incorporate the following onto the bottom of the card
ELECTRICAL - COMMUNICATIONS - AUDIO - VISUAL

```html
<!DOCTYPE html>
<html lang="en">
<head>
<meta charset="utf-8">
<title>Coralwood Electrical – Business Card</title>
<link rel="stylesheet" href="https://fonts.googleapis.com/css2?family=Tinos&display=swap">
<style>
  :root {
    --card-bg: #ffffff;
    --ink: #111111;
    --wordmark: #3b3a3c;
    --accent: #eea63a;
    --pattern-light: #efefef;
    --pattern-mid: #d6d6d6;
  }
  html, body {
    margin: 0;
    padding: 0;
    width: 1200px;
    height: 800px;
    overflow: hidden;
    background: var(--card-bg);
  }
  .card {
    position: relative;
    width: 1200px;
    height: 800px;
    background: var(--card-bg);
    font-family: "Tinos", "Times New Roman", serif;
    color: var(--ink);
  }
  .brand {
    position: absolute;
    left: 142px;
    top: 110px;
    display: flex;
    align-items: center;
    gap: 26px;
  }
  .brand-square {
    width: 150px;
    height: 150px;
    background: var(--accent);
  }
  .brand-name {
    margin: 0;
    font-weight: 400;
    font-size: 54px;
    line-height: 50px;
    color: var(--wordmark);
  }
  .contact {
    position: absolute;
    left: 142px;
    top: 370px;
    margin: 0;
    font-size: 29px;
    line-height: 36px;
    font-style: normal;
  }
  .contact span { display: block; }
  .pattern-band {
    position: absolute;
    left: 838px;
    top: 95px;
    width: 302px;
    height: 605px;
  }
  .services {
    position: absolute;
    right: 269px;
    top: 568px;
    margin: 0;
    padding: 0;
    list-style: none;
    font-size: 28px;
    line-height: 30px;
    text-align: right;
  }
  .services li:nth-child(1) { margin-right: 50px; }
  .services li:nth-child(2) { margin-right: 28px; }
  .services li:nth-child(3) { margin-right: 43px; }
  .services li:nth-child(4) { margin-right: 0; }
</style>
</head>
<body>
  <main class="card">
    <header class="brand">
      <div class="brand-square"></div>
      <h1 class="brand-name">Coralwood<br>Electrical</h1>
    </header>

    <address class="contact">
      <span class="contact-name">Dominic Farrow</span>
      <span class="contact-mobile">Mobile : 0452 317 908</span>
      <span class="contact-email">email : dominic@coralwoodelectrical.com.au</span>
    </address>

    <svg class="pattern-band" viewBox="0 0 302 605" role="img" aria-label="Geometric pattern of outlined triangles forming a bold numeral shape">
      <defs>
        <linearGradient id="bandFade" x1="0" y1="0" x2="1" y2="0">
          <stop offset="0" stop-color="var(--pattern-light)"/>
          <stop offset="1" stop-color="var(--pattern-mid)"/>
        </linearGradient>
      </defs>
      <polygon fill="url(#bandFade)"
        points="92,2 302,2 302,602 107,602 107,533 67,533 67,457 0,457 0,385 132,385 132,227 0,227 0,155 47,155 47,80 92,80"/>
    </svg>

    <ul class="services">
      <li>Electrical</li>
      <li>Communications</li>
      <li>Audio</li>
      <li>Visual</li>
    </ul>
  </main>
</body>
</html>
```